Book cover design project
Tides of the Evening
A Calm Guide to Lasting Pleasure
This is a self-help sex guide aimed at men who want to learn how to masturbate to orgasm as often as they want to.
Health
The target audience is all sexually active men.
I have in mind a simple one-color design (blue?) making use of the alliterating three M's of the subtitle (MMM), which will also echo the sound of a person having pleasure ("mmm..") and the visual image of a man lying on his back with his knees bent. No pictures of people or objects please, just subtle graphic suggestion!

```html
<!DOCTYPE html>
<html lang="en">
<head>
<meta charset="utf-8">
<title>Tides of the Evening – Book Cover</title>
<link rel="stylesheet" href="https://fonts.googleapis.com/css2?family=Anton&family=Roboto:wght@700&display=swap">
<style>
  :root {
    --sky-light: #f4fbff;
    --sky-soft: #bfe6f9;
    --sky-mid: #6fcaf2;
    --sky-edge: #1da1e2;
    --spine-blue: #1a86cc;
    --spine-edge: #1a7fc2;
    --deep-blue: #1565b0;
    --white: #ffffff;
  }
  html, body {
    margin: 0;
    padding: 0;
    width: 1200px;
    height: 828px;
    overflow: hidden;
    background: var(--white);
  }
  .cover {
    position: relative;
    width: 1200px;
    height: 828px;
    overflow: hidden;
  }
  .back-cover {
    position: absolute;
    left: 0; top: 0;
    width: 576px; height: 828px;
    background: radial-gradient(circle at 288px 330px, var(--sky-light) 0%, var(--sky-soft) 22%, var(--sky-mid) 55%, var(--sky-edge) 100%);
  }
  .back-figure {
    position: absolute;
    left: 228px; top: 276px;
    width: 132px; height: 192px;
    border-radius: 50%;
    background: radial-gradient(ellipse at center, rgba(255,255,255,0.85) 0%, rgba(255,255,255,0.35) 55%, rgba(255,255,255,0) 80%);
  }
  .spine {
    position: absolute;
    left: 576px; top: 0;
    width: 43px; height: 828px;
    background: linear-gradient(90deg, var(--spine-edge) 0%, var(--spine-blue) 50%, var(--spine-edge) 100%);
  }
  .spine-title {
    position: absolute;
    left: 50%; top: 228px;
    transform: translateX(-50%);
    writing-mode: vertical-rl;
    font-family: 'Anton', 'Impact', sans-serif;
    font-size: 26px;
    letter-spacing: 1px;
    color: var(--white);
    white-space: nowrap;
  }
  .spine-author {
    position: absolute;
    left: 50%; top: 700px;
    transform: translateX(-50%);
    writing-mode: vertical-rl;
    font-family: 'Roboto', Arial, sans-serif;
    font-weight: 700;
    font-size: 12px;
    color: rgba(255,255,255,0.35);
    white-space: nowrap;
  }
  .front-cover {
    position: absolute;
    left: 619px; top: 0;
    width: 581px; height: 828px;
    background: radial-gradient(circle at 280px 400px, var(--sky-light) 0%, var(--sky-soft) 22%, var(--sky-mid) 55%, var(--sky-edge) 100%);
  }
  .title {
    position: absolute;
    left: 74px; top: 78px;
    margin: 0;
    font-family: 'Anton', 'Impact', sans-serif;
    font-weight: 400;
    font-size: 140px;
    line-height: 156px;
    color: var(--white);
    text-transform: uppercase;
    white-space: nowrap;
    text-shadow: 4px 5px 6px rgba(0, 40, 90, 0.35);
  }
  .title span { display: block; }
  .sound-word {
    position: absolute;
    left: 74px; top: 564px;
    font-family: 'Anton', 'Impact', sans-serif;
    font-size: 92px;
    line-height: 90px;
    color: var(--deep-blue);
    letter-spacing: 2px;
    text-shadow: 3px 4px 5px rgba(0, 40, 90, 0.3);
  }
  .subtitle {
    position: absolute;
    left: 77px; top: 668px;
    font-family: 'Roboto', Arial, sans-serif;
    font-weight: 700;
    font-size: 19px;
    color: var(--white);
    white-space: nowrap;
  }
  .author {
    position: absolute;
    left: 77px; top: 772px;
    font-family: 'Roboto', Arial, sans-serif;
    font-weight: 700;
    font-size: 19px;
    color: var(--white);
    white-space: nowrap;
  }
</style>
</head>
<body>
  <div class="cover">
    <section class="back-cover">
      <div class="back-figure" role="img" aria-label="Faint white line sketch of a reclining figure with bent knees"></div>
    </section>

    <section class="spine">
      <div class="spine-title">TIDES OF THE EVENING&nbsp;&nbsp;AHH...</div>
      <div class="spine-author">By Marten 47</div>
    </section>

    <section class="front-cover">
      <h1 class="title"><span>Tides of</span><span>the</span><span>Evening</span></h1>
      <div class="sound-word">AHH...</div>
      <div class="subtitle">A Calm Guide to Lasting Pleasure</div>
      <div class="author">By Marten 47</div>
    </section>
  </div>
</body>
</html>
```